Pack Design for High Quality Marine Collagen Powder

We're looking for a quality full pack design (front and back) to sell on Brindova. We need a 2D version of front and back image in photoshop and JPG. We also need a 3D version of front and back for marketing purposes.

As many colour as needed, printing is CMYK + White digital printed.

Front of pack:

Text as follows:

Headline: 'Wild Marine Hydrolysed Collagen Powder' ...(The emphasis needs to be on the word Collagen)

Text: Essential Protein For Muscle, Hair and Skin | Rich in Amino Acids | Certified KWR Sustainably Sourced | Yeast & Gluten Free | No Additives | Unflavoured and Odorless | Water-Soluble

200g

(KWR and Sustainable logos)

Pramuvents logo at the bottom of pack. Doesn't need to be too prominent.

Back of pack:

Ingredients:
100% Pure Hydrolysed Marine Collagen (Natural)
Derived from Fish

Nutritional Information: (Please put this into a table)
Typical Values Per 10g Serving
Energy 159Kj/38kCal
Protein 9.5g
Carbohydrates 0.02g
Of which sugars 0.02g
Fat 0g
Fibre 0g
Sodium 0g
Free from GMO, Fat, Carbohydrates, Purine, Preservatives, Artificial colours/flavours
Amino Acids 99.9%
Of which essential 14.5%

This supplement should not be used as a substitute for a varied diet Do not exceed the recommended daily dose.

Please consult a healthcare practitioner if you are pregnant or taking prescription medicine before using this product.

Recommended daily dose

10-15g daily

Directions for use
Add 10g of powder to 250ml of cold water, coffee, smoothie, shake, juice, protein shake, porridge or soups.

To ensure optimum absorption, consume collagen powder at least 30 mins before a meal.

Storage information: Store in a cool dry place away from sunlight, moisture, and heat. Keep out of reach of animals and children. Keep contents dry. Reject if pack seal is broken.

Brindova Barcode image

To reorder, go to www.plinthavel.co.uk

Produced in the UK

More notes:

We have included the protein module design for inspiration of pack design along with some other designs that we like.

Pack dimensions 19cm (height) x 15cm (width). The top 2cm will be torn off by the user, so should not contain any key information.

Target Market(s)

Health conscious adults over 25

Industry/Entity Type

Marine

Colors

Designer to choose colors to be used in the design.

Requirements
Must have
• This product must stand out on Brindova and be seen. But not too busy in design and vivid enough to get clicks.
• Please only submit designs in 3D. We need a tight shadow to the right of the pack
• Final design needs to be high res ready to send to the printers with a normal bleed space around the edge.
Nice to have
• The final design should communicate quality, sustainability. The background should be clear - white ideally. Collagen is a product for health - specifically for skin and bone health.
• To help us choose, we would appreciate if you photoshop your design in 3D into an Brindova listings page - so we can see that it stands out.
Should not have
• Be too busy. Can't be bland. Text must be very readable.

```html
<!DOCTYPE html>
<html lang="en">
<head>
<meta charset="utf-8">
<title>Wild Marine Hydrolysed Collagen Protein Powder – Pack Front</title>
<link href="https://fonts.googleapis.com/css2?family=Montserrat:wght@800&family=Roboto:wght@400;500&display=swap" rel="stylesheet">
<style>
  :root {
    --backdrop: #a3b7ba;
    --pack: #f4f5f5;
    --pack-edge: #e2e5e6;
    --teal: #179b93;
    --teal-soft: #4fb8b0;
    --ink: #6a6d6f;
    --ink-dark: #3d4042;
    --sea-light: #cfecea;
    --sea-mid: #7fd0c9;
    --badge: #1e9a92;
  }
  * { margin: 0; padding: 0; box-sizing: border-box; }
  html, body { width: 1200px; height: 900px; overflow: hidden; }
  body {
    background: var(--backdrop);
    font-family: "Roboto", sans-serif;
    position: relative;
  }
  .pack {
    position: absolute;
    left: 331px; top: 55px;
    width: 538px; height: 790px;
    background: var(--pack);
    border: 1px solid var(--pack-edge);
  }
  .pack__tear-line {
    position: absolute;
    left: 0; right: 0; top: 90px;
    height: 1px;
    background: var(--pack-edge);
  }
  .headline {
    position: absolute;
    left: 0; right: 0; top: 155px;
    text-align: center;
  }
  .headline__pre,
  .headline__post {
    color: var(--ink);
    font-weight: 400;
    letter-spacing: 2px;
  }
  .headline__pre { font-size: 23px; }
  .headline__post { font-size: 29px; letter-spacing: 4px; margin-top: 2px; }
  .headline__main {
    font-family: "Montserrat", sans-serif;
    font-weight: 800;
    font-size: 62px;
    line-height: 1;
    color: var(--teal);
    letter-spacing: 1px;
    margin-top: 4px;
  }
  .sea-scene {
    position: absolute;
    left: 100px; top: 309px;
    width: 338px; height: 170px;
    background: radial-gradient(ellipse at center, var(--sea-mid) 0%, var(--sea-light) 55%, var(--pack) 78%);
  }
  .benefits {
    position: absolute;
    left: 50px; right: 50px; top: 506px;
    text-align: center;
    font-size: 12px;
    line-height: 21px;
    color: var(--ink);
    letter-spacing: 0.3px;
  }
  .benefits .sep { color: var(--teal); padding: 0 2px; }
  .benefits .accent { color: var(--teal-soft); }
  .brand {
    position: absolute;
    left: 95px; top: 637px;
    font-size: 19px;
    color: var(--ink-dark);
  }
  .brand__sub {
    display: block;
    font-size: 10px;
    text-align: right;
    margin-top: -1px;
  }
  .weight {
    position: absolute;
    left: 180px; top: 688px;
    font-size: 15px;
    font-weight: 500;
    color: var(--teal);
  }
  .cert-badge {
    position: absolute;
    left: 344px; top: 638px;
    width: 100px; height: 70px;
    border: 1px solid #b9bcbd;
    display: flex; align-items: center; justify-content: center;
  }
  .cert-badge__mark {
    width: 88px; height: 50px;
    background: var(--badge);
  }
</style>
</head>
<body>
  <main class="pack">
    <div class="pack__tear-line"></div>

    <header class="headline">
      <p class="headline__pre">WILD MARINE HYDROLYSED</p>
      <h1 class="headline__main">COLLAGEN</h1>
      <p class="headline__post">PROTEIN POWDER</p>
    </header>

    <div class="sea-scene" role="img" aria-label="Sketched seascape with sailing boats on turquoise water under a cloudy sky"></div>

    <p class="benefits">
      Essential Protein For Muscle, Hair and Skin <span class="sep">|</span> Rich in Amino Acids <span class="sep">|</span><br>
      Certified KWR Sustainably Sourced <span class="sep">|</span> <span class="accent">Yeast &amp; Gluten Free</span> <span class="sep">|</span> No Additives <span class="sep">|</span><br>
      Unflavoured and Odorless <span class="sep">|</span> Water-Soluble
    </p>

    <div class="brand">Pramuvents<span class="brand__sub">Health Products</span></div>
    <div class="weight">200g</div>

    <div class="cert-badge" role="img" aria-label="Certification badge">
      <div class="cert-badge__mark"></div>
    </div>
  </main>
</body>
</html>
```